Web Design Wecangrowbright

Overview: To develop web site with 1 main page and 1 sample inside page. Site already exists, but has been put offline. Content has been fully rewritten. If I like your style, I will pay extra for additional inside pages.
WHO I AM?
www.wecangrowbright.org was originally created to become an online community for people to use my online tools, researches, and findings to learn how to become happier.
Today, my primary services is “health coaching and lifestyle specialist.” I’m a food specialist suggesting customized solutions for my clients to eat better, how to eat, cook, groceries shop, lose weight, reduce craving, and reverse diseases.
My edge is when a suggest food I explain Why such food hurts them (or make them sick –or reason of diseases) or how the food I suggest can heal them, strengthen them, or make them lose weight. My connection to food is medical and directly impacts my client’s health.
I want to be seen as a professional in clinical nutrition and as a guru in overall wellbeing.
I coach my clients’ lifestyle as a WHOLE, introducing them to new food, fitness, and teaching them techniques to better cope with life. I study their overall health, history, and treatments, diseases, allergies as a WHOLE, connecting all medical specialties.
My services:
I sell coaching sessions, for 1 hour, 2/month for a total program of 6 months. During the sessions, I not only coach client on nutrition, but also on career, relationship, fitness, goals, and the reasons why people can’t achieve their dreams, or how to remove stress or re-organize their lives.
Future services: I may want to sell products such as T-shirts and other promotional items
Payment methods: Since I sell, I’ll need paypal and credit card payment on line. I accept checks as well (they can find my address on “contact us”)
More services, near future:
As a Certified personal fitness Trainer, I will soon offer circuit training (outdoors) and boot camps in the neighborhood to get people moving, at very affordable prices. The goal of those events will be to grow my wecangrowbright community and get new clients for Health coaching.
Knowledgeable about controlling the mind, anger, and stress, I will soon offer group meditations and breathing sessions .
Objectives:
The goal of the site are:
• To entice visitors to become my clients. The look of the site needs to reflect my customized services.
• To offer to spend an hour with client for a free health history.
• To post videos about cooking videos, discussing a theme (sugar craving, which Carbs is good for me?)
• After I meet people and give them my business cards, as they visit my site, they needs to feel impressed by the caliber of expertise.
Schedules and Budget:
Target due date is 1 week from submission of my project. During that phase, I’d like to see a wireframe, colors, styles, incorporating my logo, suggesting pictures. I would like designed tabs, access to videos, and photo library.
Motivations for people to become CLIENTS:
I think what would make people want to get my services is if they see me as an expert in holistic weight loss, someone that they can share their life, thrust, and speak at length without being judged. Visuals are crucial to simply explain effect of food on the body (needs videos main page and archive videos on various topics)
Overall, the emotions we can play with - (key words) feeling energized, feeling strong, in control of your life, a holitistic approach to a new healthy lifestyle, Balance mind, fitness, and diet, take responsibility for your own life, feeling lighter, happier, more peaceful.
Key issues of my clients:
Weight issues, high blood pressure, depression, anxiety, stress, don’t know and what to cook, suffer from diabetes, celiac, digestive diseases. People are fatigued or can’t sleep. They are addicted to sugar, coffee, fast food, speedy life.
Another issue is finding time to eat better, making exercise a routine, making the time to remove stress and enjoy life.
How do I solve clients’ problems?:
Rather than being treated by various medical specialists, I look over their Overall health since childhood. I try to find triggers of their sicknesses that often originate from their lifestyle (stress, lack of exercise, eating junk, allergies) and I recommend life modification, introduce new food, exercise , and help them shuffle their lives around. My approach is extremely customized and always requires Hours of research on my side to fully guide a client.
Demographics:
Teenagers, singles, families, young mothers. Most of clients come with weight issues, some may come to reduce cravings.
Key Messages:
The main page (please find attached “wireframe”) shall give the visitor a sense he found the guru in holistic health. Whatever medical concern they have or struggle will finally be taken care of. Someone loves them and truly cares. Food knowledge is medical, flavor, and based on client’s own taste and willingness to try. The overall feel needs to be sleek and professional.
Call to Action
Ideally, I want people to e-mail me their filled up health history (can download blank men or women health history form) so I can schedule an appointment with them (the best solution for me)
People can also call me. Since calling me is for general questions about my program, I would prefer the e-mail version whereby clients send me their health history.
Creative Considerations
Layout – considerations in accordance to brand guidelines
Need suggetions!
Tone –
Expert in clinical food and holistic health.
Visual
Color palette : I’m not sure, but the background could be light gray (clinical health), golden desert, sahara desert, earthy, pottery (well being) warm colors (orange to warm brown) or other suggestion?
Photography: I thought about flash picture. 1 picture as banner with a message on it. About 3 pictures rotate randomly.
Picture A: is “holistic food, green vegetables, natural edible roots, or cruciferous vegetables, a platter of fresh fruits and vegies, or fresh market (spices, roots, fruits and vegies). Picture needs to be crisp clear.
Picture B: Ideally: a lady fitness trainer training group exercise outdoors, in a park, or a group of people exercising outside, people look happy, boot camp training, circuit training as a group
Picture C: a picture representing the soul ,meditation, a person relaxing next to beach or in forest, next to flowers or lushy plants, a person re-energizing.
Logo: attached as separate files with various backgrounds
Icons: may look cool to use vegies or weight, happy face, or ginger root…
typography, graphics: need suggestions!

Resources
• I have an existing website name “wecangrowbright.org” the site has been put out of internet since we were trying to change it. Let me know if you need to access site. Content of the site is ineffective.
• All content has been written. You can suggest layouts and tabs
Updates

Target Market(s)

My industry is Health care, holistic Health (no medications, no supplements, no surgeries)
Buyer’s Type could be anyone wanting to lose weight, feel better, reduce stress, learn to eat, to cook, to groceries shop. My buyers are confused about all diets.My audience is people WHO WANT change in their lives. Some people know they should eat better, they mostly need support and motivation.
Typical buyer is someone who wants a new chance, a new life!
My primary target buyer is:
1. Family. I wish to coach the entire family into healthier eating and teach them how to cook and eat as a family by changing their habits.
My secondary markets are:
1.Teenagers (often eating emotionally and confused about diets)

Industry/Entity Type

Requirements
Must have
• • Format – web, print, video, sound
I would like videos (youtube connect) – facebook connect – calendar (I will update) – I will update my content, videos, and photo library regularly – people should be able to e-mail me from site – maybe be able to go through web conference. 2 different words or pdf forms shall be available for download or online filling, then they should be able to e-mail forms through site or through their personal mail system. They can also print and mail it to me.
Managing the site:
I would like to upload videos, pictures and text freely and easily. I would like to manage and update content
Nice to have
• would look cool to use entire background as a super picture!

```html
<!DOCTYPE html>
<html lang="en">
<head>
<meta charset="utf-8">
<title>Wecangrowbright – Health Coaching</title>
<link href="https://fonts.googleapis.com/css2?family=Lato:wght@300;400;700&family=Arimo:wght@400;700&display=swap" rel="stylesheet">
<style>
:root{
  --page-bg:#f1f1f1;
  --green:#3a9a47;
  --green-light:#8cc63f;
  --yellow:#fdc20f;
  --orange:#ff5a14;
  --ink:#1d1d1d;
  --text-grey:#8a8a8a;
  --text-dark:#333;
  --white:#fff;
  --footer:#0d0d0d;
  --footer-accent:#fdc20f;
}
*{box-sizing:border-box;margin:0;padding:0}
html,body{width:1200px;height:1166px;overflow:hidden}
body{background:var(--page-bg);font-family:"Arimo",Arial,sans-serif;color:var(--text-dark);position:relative}
.abs{position:absolute}

/* top utility bar */
.social{left:805px;top:40px;display:flex;gap:3px}
.social span{width:18px;height:18px;background:#3b6fb6;display:block}
.social span:nth-child(3){background:#f08a24}
.search{left:886px;top:40px;width:137px;height:19px;border:1px solid #bcbcbc;background:var(--white);font-size:9px;color:#999;padding:3px 6px}
.search-go{left:1027px;top:40px;width:27px;height:19px;background:var(--orange);color:var(--white);font-size:9px;font-weight:700;text-align:center;line-height:19px}

/* brand */
.brand{left:152px;top:80px;height:46px;display:flex;align-items:center;gap:10px}
.brand-mark{width:42px;height:42px;border-radius:50%;background:var(--green-light)}
.brand-name{font-family:"Lato",sans-serif;font-weight:700;font-size:25px;color:var(--green);line-height:1}

/* navigation */
.main-nav{left:406px;top:68px;width:648px;height:64px;background:var(--green);display:flex}
.main-nav a{color:var(--white);text-decoration:none;font-family:"Lato",sans-serif;font-size:17px;line-height:17px;text-transform:uppercase;padding:8px 0 0 24px;position:relative}
.main-nav a.active{background:var(--green-light)}
.main-nav a+a::before{content:"";position:absolute;left:0;top:10px;height:44px;border-left:1px solid rgba(255,255,255,.55)}
.main-nav a:nth-child(1){width:129px}
.main-nav a:nth-child(2){width:119px}
.main-nav a:nth-child(3){width:120px}
.main-nav a:nth-child(4){width:108px}
.main-nav a:nth-child(5){width:172px}
.main-nav a:nth-child(2)::before{display:none}

/* hero */
.hero-photo{left:148px;top:139px;width:658px;height:333px;background:linear-gradient(120deg,#e8e9ea 0%,#cfcac4 45%,#b9aa99 70%,#8f8a86 100%)}
.hero-dots{left:437px;top:438px;display:flex;gap:5px}
.hero-dots span{width:14px;height:14px;border-radius:50%;background:var(--white)}
.hero-dots span:first-child{background:var(--yellow)}
.hero-panel{left:814px;top:139px;width:240px;height:333px;background:var(--yellow);color:var(--white);font-family:"Lato",sans-serif;font-weight:300;text-align:center;padding-top:88px}
.hero-panel .l1{font-size:40px;line-height:44px;letter-spacing:-1px}
.hero-panel .l2{font-size:84px;line-height:74px;letter-spacing:-3px;font-weight:400}
.hero-panel .l3{font-size:40px;line-height:44px;letter-spacing:-1px}

/* content columns */
.video-player{left:148px;top:490px;width:222px;height:146px;background:var(--white);border:1px solid #555}
.video-player .controls{position:absolute;left:0;bottom:0;width:100%;height:16px;background:#1c1c1c}
.video-player .bar{position:absolute;left:14px;top:7px;width:110px;height:2px;background:#c1272d}
h3.section-title{font-family:"Lato",sans-serif;font-weight:700;font-size:14.5px;color:var(--ink);text-transform:uppercase}
.video-title{left:148px;top:653px}
.body-copy{font-size:10.8px;line-height:16.6px;color:var(--text-grey);text-align:justify}
.video-copy{left:148px;top:679px;width:222px}
.article-title{left:397px;top:490px}
.article{left:397px;top:517px;width:312px}
.article .lead{font-size:10.8px;line-height:16.6px;color:var(--ink);text-align:justify}
.article .byline{font-size:10.8px;font-weight:700;color:var(--orange);margin:16px 0 13px}
.scroll-rail{left:720px;top:490px;width:11px;height:293px;background:var(--orange);border-radius:6px}
.scroll-thumb{left:722px;top:556px;width:7px;height:106px;background:var(--white);border-radius:3px}
.testimonials-title{left:756px;top:490px}
.testimonials{left:756px;top:516px;width:298px}

/* client login band */
.login-band{left:148px;top:802px;width:906px;height:76px;background:var(--yellow);text-align:center;font-family:"Lato",sans-serif;font-size:15.5px;line-height:22px;color:var(--ink);padding-top:15px;letter-spacing:-.2px}
.login-band b{font-weight:700}

/* feature cards */
.card{top:914px;width:165px;height:147px;background:var(--yellow)}
.card h4{font-family:"Lato",sans-serif;font-weight:400;font-size:17.5px;line-height:18px;color:var(--ink);text-align:center;margin-top:16px;letter-spacing:-.4px}
.card .art{position:absolute;left:38px;top:62px;width:90px;height:78px;border-radius:8px}
.card-community{left:148px}
.card-community .art{background:linear-gradient(#f2c9a0,#4f8fd1)}
.card-newsletter{left:331px}
.card-newsletter .art{background:linear-gradient(#fafafa,#bdbdbd)}
.card-calendar{left:517px}
.card-calendar .art{background:linear-gradient(#3d7fd0 0 30%,#f7f7f7 30%)}
.card-blog{left:703px}
.card-blog .art{background:linear-gradient(90deg,#2f77c6,#e9eef3)}
.card-forms{left:888px}
.card-forms .art{background:radial-gradient(circle at 50% 55%,#e52521,#9c1313);border-radius:45%}

/* footer */
.site-footer{left:0;top:1114px;width:1200px;height:52px;background:var(--footer);font-size:11.5px;font-weight:700;color:var(--white)}
.site-footer .contact{position:absolute;left:150px;top:20px}
.site-footer .phone{position:absolute;right:146px;top:20px}
.site-footer em{font-style:normal;color:var(--footer-accent)}
</style>
</head>
<body>

<div class="abs social" aria-label="Social links"><span></span><span></span><span></span><span></span></div>
<div class="abs search">Search.........</div>
<div class="abs search-go">GO</div>

<div class="abs brand">
  <span class="brand-mark"></span>
  <span class="brand-name">Wecangrowbright</span>
</div>

<nav class="abs main-nav">
  <a class="active" href="#">Your<br>Coaching<br>Program</a>
  <a href="#">Why a<br>Health<br>Coach</a>
  <a href="#">About<br>Your<br>Coach</a>
  <a href="#">Recipe</a>
  <a href="#">Body<br>&amp; Mind<br>Workouts</a>
</nav>

<div class="abs hero-photo" role="img" aria-label="Photo of people stretching with arms extended in a bright gym"></div>
<div class="abs hero-dots"><span></span><span></span><span></span><span></span></div>
<div class="abs hero-panel">
  <div class="l1">LET'S MEET</div>
  <div class="l2">NEXT</div>
  <div class="l3">THURSDAY</div>
</div>

<div class="abs video-player">
  <svg style="position:absolute;left:100px;top:52px" width="22" height="24" viewBox="0 0 22 24"><path d="M2 1 L21 12 L2 23 Z" fill="#111"/></svg>
  <div class="controls">
    <svg style="position:absolute;left:4px;top:4px" width="6" height="8"><path d="M0 0 L6 4 L0 8Z" fill="#fff"/></svg>
    <span class="bar"></span>
    <svg style="position:absolute;right:8px;top:4px" width="40" height="8"><rect x="0" y="3" width="14" height="2" fill="#c1272d"/><rect x="20" y="1" width="6" height="6" fill="#fff"/><text x="30" y="7" font-size="6" fill="#fff" font-family="Arial">HD</text></svg>
  </div>
</div>
<h3 class="abs section-title video-title">Video</h3>
<p class="abs body-copy video-copy">Lorem Ipsum is simply dummy text of the printing and typesetting industry. Lorem Ipsum has been the industry's standard dummy text ever since the 1500s, when an unknown printer took a galley of type and scrambled it to make a type specimen book.</p>

<h3 class="abs section-title article-title">Get Stronger, Leaner, Healthier</h3>
<div class="abs article">
  <p class="lead">Strength training is an important part of an overall fitness program. Here's what strength training can do for you and how to get started.</p>
  <p class="byline">By Riverside Clinic staff</p>
  <p class="body-copy">You know exercise is good for you. Ideally, you're looking for ways to incorporate physical activity into your daily routine. If your aerobic workouts aren't balanced by a proper dose of strength training, though, you're missing out on a key component of overall health and fitness. Despite its reputation as a "guy" or "jock" thing, strength training is important for everyone. With a regular strength training program, you can reduce your body fat, increase your lean muscle mass and burn calories more efficiently.</p>
</div>
<div class="abs scroll-rail"></div>
<div class="abs scroll-thumb"></div>

<h3 class="abs section-title testimonials-title">Testimonials</h3>
<p class="abs body-copy testimonials">Lorem Ipsum is simply dummy text of the printing and typesetting industry. Lorem Ipsum has been the industry's standard dummy text ever since the 1500s, when an unknown printer took a galley of type and scrambled it to make a type specimen book. It has survived not only five centuries, but also the leap into electronic typesetting, remaining essentially unchanged. It was popularised in the 1960s with the release of Typeline sheets containing Lorem Ipsum passages, and more recently with desktop publishing software like Pagecraft Studio including versions of Lorem Ipsum.</p>

<div class="abs login-band">
  <b>Client login :</b> get your free login to access to monthly newsletter and archived articles (anyone) as well as teleconferences<br>
  to access videos , that privilege is for clients only (please submit your e-mail address and client Number) – thanks!
</div>

<div class="abs card card-community"><h4>Wecangrowbright<br>Community</h4><div class="art" role="img" aria-label="Illustration of two community members"></div></div>
<div class="abs card card-newsletter"><h4>Newsletter</h4><div class="art" role="img" aria-label="Illustration of a stack of newspapers"></div></div>
<div class="abs card card-calendar"><h4>Calender</h4><div class="art" role="img" aria-label="Illustration of a calendar page showing May 21"></div></div>
<div class="abs card card-blog"><h4>Blog</h4><div class="art" role="img" aria-label="Illustration of a megaphone"></div></div>
<div class="abs card card-forms"><h4>Health History<br>Forms</h4><div class="art" role="img" aria-label="Illustration of a strawberry"></div></div>

<footer class="abs site-footer">
  <span class="contact"><em>Contact Us :</em> marla@wecangrowbright.org</span>
  <span class="phone"><em>Phone :</em> 555 - 014 - 2297</span>
</footer>

</body>
</html>
```